Alaska Law Firm Needs a Sticker Design

We need a design for stickers to put on already-printed brochures. We mail the brochures to potential clients so they can learn more about accident-induced injuries, insurance claims, legal representation, and our own law firm.

One of our lawyers wrote a book that provides a helpful overview of personal injury claims. We are offering this book for free to anyone who calls and requests it. Therefore, the sticker design should include one of the following phrases, or something very similar:
a) "Still have questions? Call and request our book-- for free!"
b) "Still have questions about auto accident claims? Call and request our book today."
c) "Still have questions about filing a claim? Call and request a free copy of our book."
d) "Still have questions? Call us today to request a free copy of our book, Clear Lanes Ahead."
e) "To learn more about automobile accidents and insurance, call today and request a free copy of our book."

The sticker should be approximately 3"x3" and may be a circle, square, rectangle, or ellipsis. The sticker will be placed on the back of the folder, which is light blue. We would like the sticker to match the color scheme of our website and the folder.

I will upload an image of the book cover as soon as I obtain it.

Industry/Entity Type

Law Firm

Font styles to use
Serif
Sans Serif

Requirements
Should not have
• Bright colors that aren't already used in the folder design. e.g. no bright orange, pink, chartreuse, turquoise, yellow, red.

```html
<!DOCTYPE html>
<html lang="en">
<head>
<meta charset="utf-8">
<title>Book Offer Sticker Concepts</title>
<link href="https://fonts.googleapis.com/css2?family=Oswald:wght@700&family=Roboto:ital,wght@0,300;0,400;0,700;1,300;1,700&display=swap" rel="stylesheet">
<style>
  :root {
    --navy: #0b355f;
    --blue: #1f6aa6;
    --glow: #3a8ccb;
    --band: #4a4a4f;
    --band-edge: #c9ccd2;
    --white: #ffffff;
    --paper: #ffffff;
    --book-a: #2f5f8e;
    --book-b: #7aa8c9;
    --icon-shade: #dfe6ee;
  }
  * { box-sizing: border-box; margin: 0; padding: 0; }
  html, body { width: 1200px; height: 800px; overflow: hidden; background: var(--paper); }
  .sheet { position: relative; width: 1200px; height: 800px; }
  .sticker {
    position: absolute; width: 342px; height: 342px; border-radius: 14px; overflow: hidden;
    background: radial-gradient(circle at 50% 68%, var(--glow) 0%, var(--blue) 35%, var(--navy) 85%);
    color: var(--white); font-family: "Roboto", Arial, sans-serif;
  }
  .col-1 { left: 29px; } .col-2 { left: 429px; } .col-3 { left: 829px; }
  .row-1 { top: 29px; } .row-2 { top: 429px; }
  .headline { position: absolute; left: 0; right: 0; text-align: center; font-weight: 300; }
  .lead { display: block; font-weight: 300; font-size: 21px; line-height: 26px; }
  .keyword { display: block; font-family: "Oswald", Impact, sans-serif; font-weight: 700; font-size: 38px; line-height: 48px; letter-spacing: .3px; }
  .keyword .soft { color: var(--icon-shade); opacity: .7; }
  .question-badge {
    position: absolute; left: 114px; top: 129px; width: 114px; height: 114px; border-radius: 50%;
    background: var(--white); color: var(--blue); text-align: center;
    font-family: "Oswald", Impact, sans-serif; font-weight: 700; font-size: 92px; line-height: 110px;
  }
  .art { position: absolute; border-radius: 10px; background: radial-gradient(ellipse at center, rgba(255,255,255,.85) 0%, rgba(255,255,255,.35) 60%, rgba(255,255,255,0) 100%); }
  .art-crash-a { left: 61px; top: 123px; width: 221px; height: 112px; }
  .art-crash-b { left: 74px; top: 127px; width: 195px; height: 112px; }
  .art-form { left: 123px; top: 127px; width: 140px; height: 123px; background: linear-gradient(135deg, #f4f4f4 0%, #cfd3d8 70%, #5a5e64 100%); border-radius: 4px; }
  .art-stamp { left: 63px; top: 108px; width: 212px; height: 92px; transform: rotate(-3deg); }
  .stamp-query {
    position: absolute; left: 268px; top: 159px; width: 52px; height: 52px; border-radius: 50%;
    background: var(--white); color: var(--navy); text-align: center;
    font-family: "Oswald", Impact, sans-serif; font-weight: 700; font-size: 40px; line-height: 50px;
  }
  .offer-band { position: absolute; left: 0; right: 0; bottom: 0; height: 73px; background: var(--band); border-top: 2px solid var(--band-edge); }
  .offer-band.tall { height: 91px; }
  .offer-text { position: absolute; left: 25px; top: 8px; }
  .offer-call { display: block; font-weight: 700; font-size: 16.5px; line-height: 20px; }
  .offer-book { display: block; font-weight: 700; font-style: italic; font-size: 23px; line-height: 28px; }
  .offer-book .thin { font-weight: 300; }
  .offer-text.long { top: 5px; font-size: 16.5px; line-height: 21px; }
  .offer-text.long .line { display: block; }
  .offer-text.long em { font-weight: 700; }
  .offer-text.long .light { font-weight: 300; }
  .book-cover {
    position: absolute; left: 256px; top: 238px; width: 62px; height: 80px; transform: rotate(9deg);
    background: linear-gradient(180deg, #f3f5f8 0 18%, var(--book-a) 18% 60%, var(--book-b) 60% 92%, #f3f5f8 92% 100%);
    border: 2px solid var(--white); box-shadow: 2px 3px 5px rgba(0,0,0,.45);
  }
  .pointer { position: absolute; left: 0; top: 0; width: 342px; height: 342px; pointer-events: none; }
</style>
</head>
<body>
<main class="sheet">

  <section class="sticker col-1 row-1">
    <h2 class="headline" style="top:44px"><span class="lead">Still Have</span><span class="keyword">Questions</span></h2>
    <div class="question-badge" aria-hidden="true">?</div>
    <div class="offer-band"><p class="offer-text"><span class="offer-call">Call And Request Our</span><span class="offer-book">BOOK <span class="thin">for</span> FREE!</span></p></div>
    <svg class="pointer" viewBox="0 0 342 342" aria-hidden="true"><path d="M200 318 Q228 316 245 302" fill="none" stroke="#fff" stroke-width="2.5"/><path d="M239 297 L252 296 L248 309 Z" fill="#fff"/></svg>
    <div class="book-cover" role="img" aria-label="Cover of the free book"></div>
  </section>

  <section class="sticker col-2 row-1">
    <h2 class="headline" style="top:17px"><span class="lead">Still Have Questions</span><span class="lead">About Auto Accident</span><span class="keyword">Claims</span></h2>
    <div class="art art-crash-a" role="img" aria-label="Illustration of two cars colliding head-on"></div>
    <div class="offer-band"><p class="offer-text"><span class="offer-call">Call And Request Our</span><span class="offer-book">BOOK <span class="thin">for</span> FREE!</span></p></div>
    <svg class="pointer" viewBox="0 0 342 342" aria-hidden="true"><path d="M200 318 Q228 316 245 302" fill="none" stroke="#fff" stroke-width="2.5"/><path d="M239 297 L252 296 L248 309 Z" fill="#fff"/></svg>
    <div class="book-cover" role="img" aria-label="Cover of the free book"></div>
  </section>

  <section class="sticker col-3 row-1">
    <h2 class="headline" style="top:17px"><span class="lead">Still Have Questions</span><span class="lead">About Filing a</span><span class="keyword">Claims</span></h2>
    <div class="art art-form" role="img" aria-label="Illustration of a claim form with a pencil"></div>
    <div class="offer-band"><p class="offer-text"><span class="offer-call">Call And Request Our</span><span class="offer-book">BOOK <span class="thin">for</span> FREE!</span></p></div>
    <svg class="pointer" viewBox="0 0 342 342" aria-hidden="true"><path d="M200 318 Q228 316 245 302" fill="none" stroke="#fff" stroke-width="2.5"/><path d="M239 297 L252 296 L248 309 Z" fill="#fff"/></svg>
    <div class="book-cover" role="img" aria-label="Cover of the free book"></div>
  </section>

  <section class="sticker col-1 row-2">
    <h2 class="headline" style="top:44px"><span class="lead">Still Have</span><span class="keyword">Questions</span></h2>
    <div class="question-badge" aria-hidden="true">?</div>
    <div class="offer-band tall"><p class="offer-text long"><span class="line light">Call Us Today To Request</span><span class="line"><em>A FREE COPY</em> <i class="light">Of Our</i> <em>BOOK</em>,</span><span class="line light">Clear Lanes Ahead.</span></p></div>
    <svg class="pointer" viewBox="0 0 342 342" aria-hidden="true"><path d="M182 312 Q215 316 244 304" fill="none" stroke="#fff" stroke-width="2.5"/><path d="M238 298 L252 300 L244 311 Z" fill="#fff"/></svg>
    <div class="book-cover" role="img" aria-label="Cover of the free book"></div>
  </section>

  <section class="sticker col-2 row-2">
    <h2 class="headline" style="top:17px"><span class="lead">To Learn More About</span><span class="lead">Automobile Accidents And</span><span class="keyword">Insurance<span class="soft">?</span></span></h2>
    <div class="art art-crash-b" role="img" aria-label="Illustration of a car crash with debris"></div>
    <div class="offer-band"><p class="offer-text"><span class="offer-call">Call And Request Our</span><span class="offer-book">BOOK <span class="thin">for</span> FREE!</span></p></div>
    <svg class="pointer" viewBox="0 0 342 342" aria-hidden="true"><path d="M200 318 Q228 316 245 302" fill="none" stroke="#fff" stroke-width="2.5"/><path d="M239 297 L252 296 L248 309 Z" fill="#fff"/></svg>
    <div class="book-cover" role="img" aria-label="Cover of the free book"></div>
  </section>

  <section class="sticker col-3 row-2">
    <h2 class="headline" style="top:44px"><span class="lead">Still Have Questions</span><span class="lead">About Filing a</span></h2>
    <div class="art art-stamp" role="img" aria-label="Rubber stamp graphic reading claim"></div>
    <div class="stamp-query" aria-hidden="true">?</div>
    <div class="offer-band"><p class="offer-text"><span class="offer-call">Call And Request Our</span><span class="offer-book">BOOK <span class="thin">for</span> FREE!</span></p></div>
    <svg class="pointer" viewBox="0 0 342 342" aria-hidden="true"><path d="M200 318 Q228 316 245 302" fill="none" stroke="#fff" stroke-width="2.5"/><path d="M239 297 L252 296 L248 309 Z" fill="#fff"/></svg>
    <div class="book-cover" role="img" aria-label="Cover of the free book"></div>
  </section>

</main>
</body>
</html>
```